Business Card Design Project

I need a new business card design for my building/development company: Kestrel Ridge Builders.

We specialise in small sub-divisions, multi-story developments and new house builds.
We handle the whole process from concept stage right throught to a fully developed property.
Updates

Target Market(s)

people looking to develop their property and need help. New property buyers

Industry/Entity Type

House

Requirements
Must have
• My logo on both sides:
Side 1: Logo taking up whole side as per old card but with a color/style change.

Side 2: Contact page: include logo but the rest just surprise me!

All contact details will be: (and need to be changable for each employee) I'll inform you of specifics before printing.

Name Surname
Position ie. Managing director
M: insert mobile
E: insert email
P.O. Box 518, Ashwell, Vic, 3094
www.kestrelridgebuilders.com.au

Nice to have
• Colors i'd like: (not necessarily all but this is the basic idea)

Black, blue, grey, silver, white

```html
<!DOCTYPE html>
<html lang="en">
<head>
<meta charset="utf-8">
<title>Kestrel Ridge Builders – Business Card</title>
<link href="https://fonts.googleapis.com/css2?family=Didact+Gothic&display=swap" rel="stylesheet">
<style>
  :root{
    --page:#d9d9db;
    --navy-deep:#0a1a5c;
    --navy:#0f2f8f;
    --blue-mid:#1b4fb8;
    --blue-light:#3f8ee0;
    --band:#0d1547;
    --paper:#f1f2f4;
    --paper-shade:#e2e4e8;
    --ink:#1a2150;
    --white:#ffffff;
    --rule:#3a55a8;
  }
  *{margin:0;padding:0;box-sizing:border-box}
  html,body{width:1200px;height:1200px;overflow:hidden;background:var(--page)}
  body{font-family:"Didact Gothic",sans-serif;position:relative}
  .card{position:absolute;left:200px;width:800px;height:489px;box-shadow:0 10px 28px rgba(0,0,0,.25);overflow:hidden}
  .card svg.bg{position:absolute;inset:0}
  .card-front{top:62px;background:linear-gradient(135deg,var(--navy-deep),var(--navy) 55%,var(--blue-mid))}
  .front-brand{position:absolute;left:150px;top:190px;display:flex;align-items:center;gap:18px}
  .brand-mark{width:34px;height:34px;background:var(--blue-light)}
  .brand-name{font-size:48px;color:var(--white);letter-spacing:.5px;line-height:1}
  .front-tagline{position:absolute;left:202px;top:248px;font-size:17px;color:var(--white);letter-spacing:1px}
  .card-back{top:639px;background:linear-gradient(160deg,var(--paper),var(--paper-shade))}
  .back-band{position:absolute;left:0;top:0;width:100%;height:138px;background:var(--band)}
  .back-brand{position:absolute;left:200px;top:42px;display:flex;align-items:center;gap:12px}
  .back-brand .brand-mark{width:22px;height:22px;background:#9aa3c4}
  .back-brand .brand-name{font-size:32px;color:#dfe3f0}
  .back-tagline{position:absolute;left:234px;top:86px;font-size:12px;color:#c8cde0;letter-spacing:1px}
  .divider{position:absolute;left:430px;top:160px;width:1px;height:210px;background:#b9bcc6}
  .contact{position:absolute;color:var(--ink);font-size:19px;line-height:1.35}
  .contact-person{left:140px;top:182px}
  .contact-details{left:460px;top:205px}
  .row{display:flex;align-items:flex-start;gap:10px}
  .row svg{flex:none;margin-top:4px}
  .person-name{font-size:24px}
  .person-role{font-size:17px;color:#3a4166}
  .website{position:absolute;left:0;width:100%;top:410px;text-align:center;font-size:22px;color:var(--ink)}
  .accent-rule{position:absolute;height:1px;background:linear-gradient(90deg,transparent,var(--rule),transparent);top:395px}
</style>
</head>
<body>

<section class="card card-front" aria-label="Card front">
  <svg class="bg" width="800" height="489" viewBox="0 0 800 489" aria-hidden="true">
    <polygon points="330,489 620,130 800,130 800,489" fill="#1f4fb0" opacity=".35"/>
    <polygon points="480,489 700,220 800,220 800,489" fill="#2a63c9" opacity=".35"/>
    <polygon points="0,300 260,0 420,0 120,489 0,489" fill="#0b2380" opacity=".35"/>
    <polygon points="560,0 800,0 800,110 470,110" fill="#143a9c" opacity=".4"/>
  </svg>
  <div class="front-brand"><span class="brand-mark"></span><span class="brand-name">Kestrel Ridge Builders</span></div>
  <div class="front-tagline">renovation-construction-development</div>
</section>

<section class="card card-back" aria-label="Card back">
  <svg class="bg" width="800" height="489" viewBox="0 0 800 489" aria-hidden="true">
    <polyline points="470,489 640,250 800,420" fill="none" stroke="#d3d6dc" stroke-width="10"/>
    <polyline points="300,489 520,160 800,330" fill="none" stroke="#e6e8ec" stroke-width="6"/>
  </svg>
  <div class="back-band"></div>
  <div class="back-brand"><span class="brand-mark"></span><span class="brand-name">Kestrel Ridge Builders</span></div>
  <div class="back-tagline">renovation-construction-development</div>

  <div class="contact contact-person">
    <div class="row person-name">
      <svg width="16" height="16" viewBox="0 0 16 16"><rect width="16" height="16" rx="2" fill="var(--ink)"/><circle cx="8" cy="6" r="3" fill="#fff"/><rect x="3.5" y="10" width="9" height="4" rx="2" fill="#fff"/></svg>
      <span>Name Surname</span>
    </div>
    <div class="row person-role">
      <svg width="16" height="16" viewBox="0 0 16 16"><rect x="2" y="1" width="12" height="14" rx="1" fill="var(--ink)"/><rect x="4" y="4" width="8" height="1.5" fill="#fff"/><rect x="4" y="7" width="8" height="1.5" fill="#fff"/><rect x="4" y="10" width="6" height="1.5" fill="#fff"/></svg>
      <span>Position ie.<br>Managing director</span>
    </div>
  </div>

  <div class="divider"></div>

  <div class="contact contact-details">
    <div class="row">
      <svg width="16" height="16" viewBox="0 0 16 16"><rect x="4" y="1" width="8" height="14" rx="1.5" fill="var(--ink)"/><rect x="5.5" y="3" width="5" height="8" fill="#fff"/></svg>
      <span>M: insert mobile</span>
    </div>
    <div class="row">
      <svg width="16" height="16" viewBox="0 0 16 16"><rect x="1" y="3" width="14" height="10" fill="var(--ink)"/><polyline points="1,3 8,9 15,3" fill="none" stroke="#fff" stroke-width="1.4"/></svg>
      <span>E: insert email</span>
    </div>
    <div class="row">
      <svg width="16" height="16" viewBox="0 0 16 16"><path d="M8 1a5 5 0 0 0-5 5c0 4 5 9 5 9s5-5 5-9a5 5 0 0 0-5-5z" fill="var(--ink)"/><circle cx="8" cy="6" r="2" fill="#fff"/></svg>
      <span>P.O. Box 518, Ashwell,<br>Vic, 3094</span>
    </div>
  </div>

  <div class="accent-rule" style="left:40px;width:220px"></div>
  <div class="accent-rule" style="left:540px;width:220px"></div>
  <div class="website">www.kestrelridgebuilders.com.au</div>
</section>

</body>
</html>
```